Communications & Broadcast Consulting/PR/Media Relations & Public Affairs

My main goals are to provide communications support to school districts, small towns/cities/hospitals and private businesses in the form of press releases, media relations, public affairs. I also have 25 years experience as a television news anchor/reporter and I'm open to free-lance reporting in both Indianapolis and other markets. My specialty is working with the media.
Communications

```html
<!DOCTYPE html>
<html lang="en">
<head>
<meta charset="utf-8">
<title>Ridgeline Communications – Business Card</title>
<link rel="stylesheet" href="https://fonts.googleapis.com/css2?family=Open+Sans:wght@400;600&display=swap">
<style>
  :root {
    --stage: #3a3a3a;
    --card-white: #ffffff;
    --card-black: #1c1c1c;
    --ink: #222222;
    --green: #14b14b;
    --green-soft: #6cc04a;
    --emblem-light: #d9efe0;
    --emblem-dark: #2f4a37;
    --rule: #9a9a9a;
  }
  * { box-sizing: border-box; margin: 0; padding: 0; }
  html, body { width: 1200px; height: 750px; overflow: hidden; }
  body {
    background: var(--stage);
    font-family: "Open Sans", Arial, sans-serif;
    color: var(--ink);
    position: relative;
  }
  .card {
    position: absolute;
    top: 210px;
    width: 511px;
    height: 294px;
    border-radius: 20px;
    overflow: hidden;
    background: var(--card-white);
  }
  .card-front { left: 78px; }
  .card-back { left: 609px; }

  .emblem-area {
    position: absolute;
    border-radius: 6px;
    background: linear-gradient(90deg, var(--emblem-light) 0%, var(--green-soft) 50%, var(--emblem-dark) 100%);
  }

  /* Front */
  .front-dark-half {
    position: absolute;
    top: 0; right: 0; bottom: 0;
    width: 255px;
    background: var(--card-black);
  }
  .front-emblem { left: 152px; top: 38px; width: 210px; height: 92px; }
  .front-wordmark {
    position: absolute;
    left: 32px;
    top: 190px;
    font-weight: 400;
    color: var(--ink);
  }
  .front-wordmark .name-line { display: block; font-size: 38px; line-height: 46px; }
  .front-wordmark .sub-line { display: block; font-size: 18px; line-height: 24px; letter-spacing: 2px; }

  /* Back */
  .back-emblem { left: 332px; top: 16px; width: 78px; height: 48px; }
  .back-wordmark {
    position: absolute;
    right: 28px;
    top: 68px;
    text-align: right;
    font-weight: 400;
    color: var(--ink);
  }
  .back-wordmark .name-line { display: block; font-size: 31px; line-height: 38px; }
  .back-wordmark .sub-line { display: block; font-size: 15px; line-height: 20px; letter-spacing: 1.6px; }

  .rule {
    position: absolute;
    left: 0; right: 0;
    height: 1px;
    background: var(--rule);
  }
  .rule-top { top: 135px; }
  .rule-bottom { top: 182px; }
  .name-band {
    position: absolute;
    left: 0; right: 0;
    top: 140px;
    height: 38px;
    background: var(--green);
    color: var(--card-white);
    display: flex;
    align-items: center;
    padding-left: 27px;
  }
  .name-band .person-name { font-size: 20px; }
  .name-band .divider {
    width: 1px; height: 22px;
    background: var(--card-white);
    margin: 0 9px;
  }
  .name-band .designation { font-size: 14px; }

  .contact-list {
    position: absolute;
    left: 27px;
    top: 194px;
    list-style: none;
    font-size: 13.5px;
    line-height: 18px;
  }
  .contact-list li { display: flex; align-items: center; }
  .contact-list svg { width: 11px; height: 11px; margin-right: 12px; fill: var(--ink); }
  .address {
    position: absolute;
    right: 30px;
    top: 194px;
    font-size: 13.5px;
    line-height: 18px;
    display: flex;
    align-items: center;
  }
  .address svg { width: 10px; height: 12px; margin-left: 3px; fill: var(--ink); }
  .back-swoosh { position: absolute; left: 0; bottom: 0; width: 511px; height: 294px; }
</style>
</head>
<body>
  <section class="card card-front" aria-label="Card front">
    <div class="front-dark-half"></div>
    <div class="emblem-area front-emblem" role="img" aria-label="Company emblem area: signal tower with broadcast waves"></div>
    <p class="front-wordmark"><span class="name-line">Ridgeline</span><span class="sub-line">Communications</span></p>
  </section>

  <section class="card card-back" aria-label="Card back">
    <div class="emblem-area back-emblem" role="img" aria-label="Small company emblem area: signal tower with broadcast waves"></div>
    <p class="back-wordmark"><span class="name-line">Ridgeline</span><span class="sub-line">Communications</span></p>
    <div class="rule rule-top"></div>
    <div class="name-band">
      <span class="person-name">your name</span>
      <span class="divider"></span>
      <span class="designation">designation</span>
    </div>
    <div class="rule rule-bottom"></div>

    <ul class="contact-list">
      <li>
        <svg viewBox="0 0 12 12" aria-hidden="true"><path d="M1 3.5C1 2 3 1.5 6 1.5s5 .5 5 2v1H8.5v-1h-5v1H1z"/><path d="M2 6l1.5-1.5h5L10 6v4.5H2z"/></svg>
        IN 46201 317.555.0142
      </li>
      <li>
        <svg viewBox="0 0 12 12" aria-hidden="true"><path d="M3 0h6v12H3zM4 1.2v8.6h4V1.2z"/></svg>
        317.555.0187
      </li>
      <li>
        <svg viewBox="0 0 12 12" aria-hidden="true"><path d="M0 2.5h12v7H0z"/><path d="M0.5 3l5.5 3.5L11.5 3" stroke="#fff" stroke-width="1" fill="none"/></svg>
        contact@ridgelinecomms.com
      </li>
    </ul>

    <p class="address">1820 Maple Crest Drive Indianapolis
      <svg viewBox="0 0 10 12" aria-hidden="true"><path d="M5 0a4.2 4.2 0 0 1 4.2 4.2C9.2 7 5 12 5 12S.8 7 .8 4.2A4.2 4.2 0 0 1 5 0zm0 2.6a1.6 1.6 0 1 0 0 3.2 1.6 1.6 0 0 0 0-3.2z"/></svg>
    </p>

    <svg class="back-swoosh" viewBox="0 0 511 294" aria-hidden="true">
      <path d="M0 256 Q210 300 511 244 L511 294 L0 294Z" fill="var(--green-soft)"/>
      <path d="M0 264 Q215 304 511 255 L511 294 L0 294Z" fill="var(--card-white)"/>
      <path d="M0 269 Q220 302 511 262 L511 294 L0 294Z" fill="var(--card-black)"/>
    </svg>
  </section>
</body>
</html>
```